Hello design crowd. 413 Stillhouse in Eagle Colorado is a new craft distillery and we need a label for our new product, "Gold Hollow Rum." Attached are some pictures of the Hollow. We are open to any and all ideas from abstract to representational. We want something bold and striking with just a few colors. Perhaps:Red like the rocks, the intense blue of the Colorado sky, white clouds, green of the evergreens and some black like our logo and bottle cap.

Reason: We need to finalize our final decision on the project. Thanks 413 Stillhouse, LLC

```html
<!DOCTYPE html>
<html lang="en">
<head>
<meta charset="utf-8">
<title>Gold Hollow Rum – Label Concept</title>
<link rel="stylesheet" href="https://fonts.googleapis.com/css2?family=Arimo:wght@400&family=Cinzel:wght@400&family=Roboto+Condensed:wght@400&display=swap">
<style>
  :root {
    --page-bg: #ffffff;
    --heading-ink: #1c1c1c;
    --label-black: #050505;
    --brand-red: #e4252b;
    --ink-white: #f4f4f4;
    --rule-grey: #8a8a8a;
    --brush-grey: #2a2d30;
    --bottle-dark: #1a1414;
    --footer-bar: #1b1b1b;
  }
  * { margin: 0; padding: 0; box-sizing: border-box; }
  html, body {
    width: 1200px;
    height: 900px;
    overflow: hidden;
    background: var(--page-bg);
  }
  .board {
    position: relative;
    width: 1200px;
    height: 900px;
  }

  /* Presentation heading */
  .board__heading {
    position: absolute;
    left: 45px;
    top: 42px;
    display: flex;
    align-items: center;
    gap: 14px;
    font-family: "Roboto Condensed", "Arial Narrow", Arial, sans-serif;
    font-size: 31px;
    line-height: 1;
    color: var(--heading-ink);
  }
  .board__divider {
    width: 2px;
    height: 40px;
    background: var(--heading-ink);
  }

  /* Bottle mockup area */
  .bottle-mockup {
    position: absolute;
    left: 187px;
    top: 192px;
    width: 188px;
    height: 543px;
  }

  /* Label */
  .label {
    position: absolute;
    left: 548px;
    top: 45px;
    width: 630px;
    height: 788px;
    background: var(--label-black);
    color: var(--ink-white);
    font-family: "Arimo", "Helvetica Neue", Arial, sans-serif;
    overflow: hidden;
  }
  .label__brand {
    position: absolute;
    top: 72px;
    left: 22px;
    right: 22px;
    display: flex;
    align-items: center;
    gap: 18px;
  }
  .label__brand::before,
  .label__brand::after {
    content: "";
    flex: 1;
    height: 1px;
    background: var(--rule-grey);
  }
  .brand-name {
    display: flex;
    align-items: center;
    gap: 10px;
    font-size: 26px;
    letter-spacing: 2px;
    line-height: 36px;
    color: var(--brand-red);
  }
  .brand-name__dot {
    width: 12px;
    height: 12px;
    border-radius: 50%;
    background: var(--brand-red);
  }
  .label__artwork {
    position: absolute;
    top: 130px;
    left: 20px;
    width: 590px;
    height: 490px;
  }
  .label__title {
    position: absolute;
    top: 170px;
    left: 0;
    right: 0;
    text-align: center;
    font-family: "Cinzel", "Trajan Pro", Georgia, serif;
    font-weight: 400;
    font-size: 70px;
    letter-spacing: 1px;
    line-height: 1;
    color: var(--ink-white);
  }
  .label__style {
    position: absolute;
    top: 612px;
    left: 0;
    right: 0;
    text-align: center;
    font-size: 54px;
    line-height: 1;
    color: var(--ink-white);
  }
  .label__footer {
    position: absolute;
    left: 22px;
    right: 22px;
    top: 726px;
    border-top: 1px solid var(--rule-grey);
    padding-top: 20px;
    display: flex;
    justify-content: space-between;
    font-size: 21px;
    line-height: 1;
    letter-spacing: 0.5px;
    color: var(--brand-red);
  }

  /* Bottom bar */
  .board__footer {
    position: absolute;
    left: 0;
    right: 0;
    bottom: 0;
    height: 45px;
    background: var(--footer-bar);
  }
</style>
</head>
<body>
  <main class="board">
    <h2 class="board__heading">
      <span>Gold Hollow Rum</span>
      <span class="board__divider"></span>
      <span>Label Concept</span>
    </h2>

    <svg class="bottle-mockup" viewBox="0 0 188 543" role="img" aria-label="Photographed dark rum bottle with two side handles wearing the black label">
      <defs>
        <linearGradient id="bottle-shade" x1="0" x2="1" y1="0" y2="0">
          <stop offset="0%" stop-color="#0c0a0a"/>
          <stop offset="50%" stop-color="var(--bottle-dark)"/>
          <stop offset="100%" stop-color="#0c0a0a"/>
        </linearGradient>
      </defs>
      <rect x="0" y="0" width="188" height="543" rx="40" fill="url(#bottle-shade)"/>
    </svg>

    <section class="label">
      <svg class="label__artwork" viewBox="0 0 590 490" role="img" aria-label="Brush-painted red eagle in flight over dark grey brush strokes">
        <defs>
          <radialGradient id="artwork-glow" cx="50%" cy="62%" r="50%">
            <stop offset="0%" stop-color="var(--brand-red)" stop-opacity="0.95"/>
            <stop offset="35%" stop-color="#a81d22" stop-opacity="0.8"/>
            <stop offset="65%" stop-color="var(--brush-grey)" stop-opacity="0.6"/>
            <stop offset="100%" stop-color="var(--label-black)" stop-opacity="0"/>
          </radialGradient>
        </defs>
        <rect width="590" height="490" fill="url(#artwork-glow)"/>
      </svg>

      <header class="label__brand">
        <span class="brand-name"><span class="brand-name__dot"></span>413 STILLHOUSE</span>
      </header>

      <h1 class="label__title">Gold Hollow</h1>

      <p class="label__style">Spiced Rum</p>

      <footer class="label__footer">
        <span class="label__volume">750 ML</span>
        <span class="label__abv">40% ALC/VOL</span>
      </footer>
    </section>

    <div class="board__footer"></div>
  </main>
</body>
</html>
```